Brackwell Immigration Law

We need a web design for our existing company www.brackwellcounsel.co.uk. We are an immigration consultancy. The final design should communicate professionalism, integrity and affordability.

Industry/Entity Type

It Company

Logo Text

Brackwell Counsel Partners

Number of Pages Required

5+ page

Font styles to use
Serif

Requirements
Must have
• I want to have the same silhouette logo but something different in positioning..
Nice to have
• Please have a look at these websites:
• https://www.travelpathguide.co.uk/visa_uk/
• http://www.oakdenadvisers.co.uk/
• http://www.myrtlegatelaw.org/index.php
• www.brackwellcounsel.co.uk

```html
<!DOCTYPE html>
<html lang="en">
<head>
<meta charset="utf-8">
<title>Brackwell Counsel Partners – Immigration Law</title>
<link href="https://fonts.googleapis.com/css2?family=Open+Sans:wght@400;600;700;800&family=Merriweather:wght@400;700&display=swap" rel="stylesheet">
<style>
:root{
  --yellow:#f5b400;
  --orange:#e59a00;
  --ink:#2b2f36;
  --muted:#6b7079;
  --line:#dcdfe4;
  --dark:#1b2029;
  --navy:#222b38;
  --paper:#ffffff;
  --soft:#f3f4f6;
}
*{box-sizing:border-box;margin:0;padding:0}
html,body{width:1200px;height:3160px;overflow:hidden;background:var(--paper)}
body{font-family:"Open Sans",Arial,sans-serif;color:var(--ink);font-size:13px;line-height:1.55}
.page{position:relative;width:1200px;height:3160px;overflow:hidden}
.h-title{font-family:"Merriweather",Georgia,serif;color:var(--orange);font-size:22px;font-weight:700;margin-bottom:6px}
.rule{height:1px;background:var(--line);margin-bottom:18px}
.sub{color:var(--orange);font-weight:700;font-size:13px;letter-spacing:.5px;margin-bottom:8px}
p{color:var(--muted);font-size:12.5px}

/* header */
.site-header{position:absolute;top:0;left:0;width:1200px;height:64px;display:flex;align-items:center;justify-content:space-between;padding:0 60px;background:#fff;border-bottom:1px solid var(--line)}
.brand{display:flex;align-items:center;gap:10px;font-family:"Merriweather",Georgia,serif;font-size:15px;font-weight:700;color:var(--ink)}
.brand-dot{width:30px;height:30px;border-radius:50%;background:var(--ink)}
.nav{display:flex;gap:4px}
.nav a{padding:8px 14px;font-size:13px;font-weight:600;color:var(--ink);text-decoration:none}
.nav a.active{background:var(--yellow);color:#fff}

/* hero */
.hero{position:absolute;top:64px;left:0;width:1200px;height:496px}
.hero-photo{position:absolute;inset:0;background:linear-gradient(120deg,#8d95a0 0%,#bfc5cc 40%,#6d7683 100%)}
.hero-panel{position:absolute;top:28px;left:770px;width:390px;height:380px;background:rgba(23,30,42,.9);padding:36px 34px;color:#fff;text-align:center}
.hero-panel h1{color:var(--yellow);font-size:19px;font-weight:800;letter-spacing:.5px}
.hero-panel h2{font-size:14px;font-weight:600;margin:4px 0 22px}
.hero-panel p{color:#e3e6ea;font-size:14px;line-height:1.7}
.btn-yellow{display:inline-block;margin-top:30px;background:var(--yellow);color:#fff;font-weight:700;font-size:12px;padding:11px 32px;border-radius:18px}

/* consult strip */
.consult{position:absolute;top:560px;left:0;width:1200px;height:100px;background:var(--dark);color:#fff;display:flex;align-items:center;padding-left:80px}
.consult-title{font-size:17px;font-weight:800;width:330px;line-height:1.3}
.consult-call{display:flex;align-items:center;gap:14px;width:390px}
.call-icon{width:46px;height:46px;border-radius:50%;border:2px solid var(--yellow);display:flex;align-items:center;justify-content:center}
.call-label{font-size:11px;font-weight:700;color:#c9ccd2}
.call-number{font-size:26px;font-weight:800;color:var(--yellow);line-height:1.1}
.call-hours{font-size:10.5px;color:#aab0b8}
.chat-box{position:absolute;right:80px;top:-12px;width:320px;height:112px;background:var(--yellow);text-align:center;padding-top:22px}
.chat-box h3{font-size:15px;font-weight:800;color:#fff}
.btn-white{display:inline-block;margin-top:10px;background:#fff;color:var(--orange);font-weight:700;font-size:12px;padding:8px 26px;border-radius:16px}

/* firm */
.firm{position:absolute;top:712px;left:80px;width:1040px;height:480px}
.firm-text{position:absolute;left:0;top:0;width:360px}
.firm-image{position:absolute;left:0;top:260px;width:360px;height:190px;background:linear-gradient(135deg,#c7cdd4,#8f98a3)}
.equality{position:absolute;left:400px;top:62px;width:260px}
.consult-form{position:absolute;left:720px;top:0;width:320px}
.field-row{display:flex;gap:10px;margin-bottom:10px}
.field{flex:1;height:32px;border:1px solid var(--line);font-size:11px;color:#9aa0a8;padding:7px 9px}
.field.msg{height:90px}
.check{display:flex;align-items:center;gap:8px;font-size:11px;color:var(--muted);margin:6px 0 12px}
.check span{width:14px;height:14px;border:1px solid #aab0b8}
.btn-dark{display:inline-block;background:var(--ink);color:#fff;font-size:12px;font-weight:700;padding:8px 22px}

/* team */
.team{position:absolute;top:1220px;left:0;width:1200px;height:400px;background:var(--navy);text-align:center;color:#fff;padding-top:36px}
.team .h-title{color:#fff}
.team-intro{color:#b9c0c9;font-size:12px;width:640px;margin:0 auto}
.team-grid{display:flex;justify-content:center;gap:140px;margin-top:30px}
.member{width:170px}
.member-photo{width:160px;height:160px;border-radius:50%;margin:0 auto 14px;background:radial-gradient(circle at 50% 40%,#8a8f96,#3b4250);border:4px solid rgba(255,255,255,.15)}
.member h4{font-size:14px;font-weight:700}
.member p{color:#b9c0c9;font-size:11px}

/* join + news */
.join{position:absolute;top:1680px;left:80px;width:640px;height:800px}
.join-text{position:absolute;left:0;top:50px;width:240px}
.join-item{position:absolute;left:260px;width:380px}
.join-photo{width:380px;height:230px;background:linear-gradient(135deg,#b5bcc5,#5f6874);margin-bottom:10px}
.join-item p{font-size:11.5px}
.news{position:absolute;top:1680px;left:780px;width:340px}
.news-item{display:flex;gap:14px;margin-bottom:46px}
.news-thumb{width:100px;height:100px;flex:none;background:linear-gradient(135deg,#d9b79b,#9c7a63)}
.news-item h5{color:var(--orange);font-size:12.5px;font-weight:700;margin-bottom:3px}
.news-item p{font-size:11px;line-height:1.45}

/* partners */
.partners{position:absolute;top:2530px;left:80px;width:1040px;display:grid;grid-template-columns:repeat(4,1fr);gap:20px}
.partner{height:90px;border:1px solid var(--line);display:flex;align-items:center;justify-content:center}
.partner span{width:120px;height:44px;background:var(--soft);border:1px solid var(--line);border-radius:4px}
.partner.round span{width:52px;height:52px;border-radius:50%}

/* footer */
.site-footer{position:absolute;top:2760px;left:0;width:1200px;height:400px;background:var(--dark);color:#c9ccd2}
.foot-col{position:absolute;top:40px}
.foot-col h6{color:#fff;font-size:13px;font-weight:800;letter-spacing:.5px;margin-bottom:14px}
.foot-links li{list-style:none;font-size:11.5px;color:#9aa1aa;margin-bottom:5px}
.blog-item{display:flex;gap:12px;margin-bottom:16px;width:330px}
.blog-thumb{width:60px;height:60px;flex:none;background:linear-gradient(135deg,#8c7a6c,#4d4440)}
.blog-item h5{color:#fff;font-size:12px;font-weight:700}
.blog-item p{color:#9aa1aa;font-size:11px}
.socials{display:flex;gap:10px;margin-bottom:14px}
.socials span{width:34px;height:34px;border-radius:50%;background:#fff}
.foot-note{color:#9aa1aa;font-size:11px;width:260px}
.copyright{position:absolute;left:860px;top:250px;font-size:11px;color:#9aa1aa}
</style>
</head>
<body>
<div class="page">

<header class="site-header">
  <div class="brand"><span class="brand-dot"></span>Brackwell Counsel Partners</div>
  <nav class="nav">
    <a class="active">Home</a><a>About Us</a><a>Join Us</a><a>Contact us</a><a>Blog</a>
  </nav>
</header>

<section class="hero">
  <div class="hero-photo" role="img" aria-label="Photo of a smiling businesswoman seated with luggage in an airport terminal"></div>
  <div class="hero-panel">
    <h1>BRACKWELL COUNSEL PARTNERS</h1>
    <h2>Immigration Law</h2>
    <p>We are Immigration Lawyers regulated by the Migration Advice Standards Board (MASB) at the highest level (Level 3) and authorised by The Advocates Guild of Albion.</p>
    <span class="btn-yellow">LEARN MORE</span>
  </div>
</section>

<section class="consult">
  <div class="consult-title">GET FREE LEGAL<br>CONSULTATION</div>
  <div class="consult-call">
    <div class="call-icon">
      <svg width="22" height="22" viewBox="0 0 24 24"><path fill="#f5b400" d="M6.6 10.8a15.1 15.1 0 0 0 6.6 6.6l2.2-2.2a1 1 0 0 1 1-.25 11.4 11.4 0 0 0 3.6.57 1 1 0 0 1 1 1V20a1 1 0 0 1-1 1A17 17 0 0 1 3 4a1 1 0 0 1 1-1h3.5a1 1 0 0 1 1 1c0 1.25.2 2.45.57 3.57a1 1 0 0 1-.25 1z"/></svg>
    </div>
    <div>
      <div class="call-label">CALL US TOLL FREE</div>
      <div class="call-number">0207 555 0184</div>
      <div class="call-hours">7 days a week<br>from 8am to 8pm</div>
    </div>
  </div>
  <div class="chat-box">
    <h3>ONLINE SUPPORT CHAT</h3>
    <span class="btn-white">Register Now</span>
  </div>
</section>

<section class="firm">
  <div class="firm-text">
    <h2 class="h-title">Our Firm</h2>
    <div class="rule"></div>
    <p>Brackwell Counsel Partners is regulated by the Migration Advice Standards Board at the highest level. Our team of dedicated advisers offers clear, honest and affordable guidance on every type of visa, settlement and citizenship matter, helping families, students and businesses move forward with confidence and peace of mind.</p>
  </div>
  <div class="firm-image" role="img" aria-label="Photo of advisers meeting with a client at a desk"></div>
  <div class="equality">
    <div class="sub">EQUALITY STATEMENT</div>
    <p>Brackwell Counsel Partners is committed to promoting equality and diversity in all its dealings with clients, staff and other professionals. We do not discriminate on grounds of age, disability, gender, race, religion or belief, sexual orientation, marital status or pregnancy.</p>
    <p style="margin-top:12px">We are committed to treating every client with fairness, dignity and respect, and we welcome feedback on how we can improve.</p>
  </div>
  <div class="consult-form">
    <h2 class="h-title">Request Consultation</h2>
    <div class="rule"></div>
    <div class="field-row"><div class="field">First Name</div><div class="field">Last Name</div></div>
    <div class="field-row"><div class="field">Email</div><div class="field">Phone</div></div>
    <div class="field-row"><div class="field">City</div><div class="field">Country</div></div>
    <div class="field-row"><div class="field msg">Message</div></div>
    <div class="check"><span></span>Please contact me by phone</div>
    <span class="btn-dark">Submit</span>
  </div>
</section>

<section class="team">
  <h2 class="h-title">Our Team</h2>
  <p class="team-intro">Our lawyers are regulated by the Migration Advice Standards Board at the highest level and authorised by The Advocates Guild of Albion.</p>
  <div class="team-grid">
    <div class="member"><div class="member-photo" role="img" aria-label="Portrait of attorney"></div><h4>Attorney 1</h4><p>Senior immigration adviser with wide experience in settlement cases.</p></div>
    <div class="member"><div class="member-photo" role="img" aria-label="Portrait of attorney"></div><h4>Attorney 2</h4><p>Specialist in work and business visa applications and appeals.</p></div>
    <div class="member"><div class="member-photo" role="img" aria-label="Portrait of attorney"></div><h4>Attorney 3</h4><p>Focused on family, spouse and student visa matters.</p></div>
  </div>
</section>

<section class="join">
  <h2 class="h-title">Join Us</h2>
  <div class="rule"></div>
  <div class="join-text">
    <div class="sub">EQUALITY STATEMENT</div>
    <p>Brackwell Counsel Partners is committed to fair and open recruitment. We welcome applications from all backgrounds and select candidates solely on merit, skills and experience.</p>
    <p style="margin-top:12px">We are proud to offer a supportive working culture, ongoing training and clear paths for career growth.</p>
    <p style="margin-top:12px">If you share our values and wish to help people build new lives in the UK, we would like to hear from you. Send your CV and a short cover letter to our recruitment team today.</p>
    <p style="margin-top:12px">Roles open throughout the year include caseworkers, paralegals, client liaison staff and qualified advisers at every level of accreditation.</p>
    <p style="margin-top:12px">All new starters receive a structured induction, a named mentor and funded study towards further professional qualifications.</p>
  </div>
  <div class="join-item" style="top:50px">
    <div class="join-photo" role="img" aria-label="Photo of a team of lawyers standing together"></div>
    <p>We are always looking for talented advisers and support staff who care about clients and justice.</p>
  </div>
  <div class="join-item" style="top:380px">
    <div class="join-photo" role="img" aria-label="Photo of colleagues discussing documents"></div>
    <p>Join a friendly team that values learning, teamwork and high professional standards in every case.</p>
  </div>
</section>

<section class="news">
  <h2 class="h-title">News &amp; Publications</h2>
  <div class="rule"></div>
  <div class="news-item"><div class="news-thumb" role="img" aria-label="Thumbnail photo"></div><div><h5>Visa Rules Update</h5><p>New guidance on family visas explained in plain terms for applicants.</p></div></div>
  <div class="news-item"><div class="news-thumb" role="img" aria-label="Thumbnail photo"></div><div><h5>Student Routes</h5><p>What changes to the student route mean for new arrivals this year.</p></div></div>
  <div class="news-item"><div class="news-thumb" role="img" aria-label="Thumbnail photo"></div><div><h5>Settlement Tips</h5><p>Key steps to prepare a strong indefinite leave to remain application.</p></div></div>
  <div class="news-item"><div class="news-thumb" role="img" aria-label="Thumbnail photo"></div><div><h5>Work Visa Guide</h5><p>How employers and workers can plan ahead for skilled worker visas.</p></div></div>
  <div class="news-item"><div class="news-thumb" role="img" aria-label="Thumbnail photo"></div><div><h5>Appeals Advice</h5><p>Understanding your rights when a visa application is refused.</p></div></div>
</section>

<section class="partners" aria-label="Accreditations">
  <div class="partner round"><span></span></div>
  <div class="partner"><span></span></div>
  <div class="partner round"><span></span></div>
  <div class="partner"><span></span></div>
  <div class="partner round"><span></span></div>
  <div class="partner"><span></span></div>
  <div class="partner round"><span></span></div>
  <div class="partner"><span></span></div>
</section>

<footer class="site-footer">
  <div class="foot-col" style="left:80px">
    <h6>IMMIGRATION LAW</h6>
    <ul class="foot-links">
      <li>Family Visas</li><li>Spouse Visas</li><li>Student Visas</li><li>Work Visas</li><li>Settlement</li><li>Citizenship</li><li>Appeals</li><li>Business Visas</li>
    </ul>
  </div>
  <div class="foot-col" style="left:460px">
    <h6>LATEST BLOG</h6>
    <div class="blog-item"><div class="blog-thumb" role="img" aria-label="Blog thumbnail photo"></div><div><h5>Now a Permanent Resident in the UK</h5><p>A client story about settling in Britain after years of hard work.</p></div></div>
    <div class="blog-item"><div class="blog-thumb" role="img" aria-label="Blog thumbnail photo"></div><div><h5>Now a Permanent Resident in the UK</h5><p>Tips and lessons from a recent successful application.</p></div></div>
  </div>
  <div class="foot-col" style="left:860px">
    <h6>FOLLOW US</h6>
    <div class="socials"><span></span><span></span><span></span><span></span><span></span></div>
    <p class="foot-note">We are Immigration Lawyers regulated by the Migration Advice Standards Board at the highest level.</p>
  </div>
  <div class="copyright">© 2024 Brackwell Counsel Partners</div>
</footer>

</div>
</body>
</html>
```